Architectural firm needs a graphic representation of our Master Planning process

We need an image to convey our 3-phase, 8-step Master Planning process that we utilize when designing plans for schools K-12. What we currently use looks very outdated in both the design and color scheme. We'd like an EPS created that can be scaled without distortion. The files I've attached show the current graphic and an instruction sheet which also contains our colors.

```html
<!DOCTYPE html>
<html lang="en">
<head>
<meta charset="utf-8">
<title>Planning Process</title>
<link rel="stylesheet" href="https://fonts.googleapis.com/css2?family=Roboto+Condensed:wght@400;700&family=Lato:wght@400;700&display=swap">
<style>
  :root {
    --bg: #efefef;
    --blue: #2467a0;
    --ink: #2b2b2b;
    --school: #1d4a5e;
    --architect: #9c1c32;
    --fundraiser: #a9a23c;
    --footer-bg: #333333;
    --footer-text: #f2f2f2;
  }
  html, body { margin: 0; padding: 0; overflow: hidden; }
  body { background: var(--bg); }
  .process-graphic {
    position: relative;
    width: 1200px;
    height: 329px;
    background: var(--bg);
    overflow: hidden;
  }
  .process-diagram { position: absolute; left: 0; top: 0; }
  .title { font-family: "Roboto Condensed", sans-serif; font-weight: 700; font-size: 21px; fill: var(--blue); letter-spacing: 0.5px; }
  .step-label { font-family: "Roboto Condensed", sans-serif; font-weight: 700; fill: var(--ink); text-anchor: middle; }
  .step-label--lead { font-size: 21px; }
  .step-label--major { font-size: 16px; }
  .step-label--minor { font-size: 12px; }
  .role-label { font-family: "Lato", sans-serif; font-size: 10.5px; fill: var(--ink); }
  .role-label--spaced { letter-spacing: 4px; }
  .role-label--tight { letter-spacing: 0.6px; font-size: 10px; }
  .icon-glyph { fill: #ffffff; }
  .icon-stroke { fill: none; stroke: #ffffff; stroke-width: 2.2; stroke-linecap: round; stroke-linejoin: round; }
  .caption {
    position: absolute;
    left: 0; top: 280px;
    width: 1200px; height: 49px;
    box-sizing: border-box;
    padding: 7px 30px 0 32px;
    background: var(--footer-bg);
    color: var(--footer-text);
    font-family: "Lato", sans-serif;
    font-size: 12.8px;
    line-height: 18px;
    margin: 0;
  }
</style>
</head>
<body>
<main class="process-graphic">
  <svg class="process-diagram" width="1200" height="280" viewBox="0 0 1200 280" aria-label="Planning process steps and responsibilities">
    <!-- heading -->
    <text class="title" x="26" y="53">PLANNING</text>
    <text class="title" x="26" y="79">PROCESS</text>

    <!-- timeline -->
    <line x1="26" y1="58" x2="1100" y2="58" stroke="var(--blue)" stroke-width="1.3"/>

    <g class="step-icons" fill="var(--blue)">
      <!-- visioning: light bulb -->
      <circle cx="221" cy="58" r="29"/>
      <g class="icon-stroke" transform="translate(221 58)">
        <path d="M-6 6 C-11 2 -11 -10 0 -11 C11 -10 11 2 6 6 L5 10 L-5 10 Z"/>
        <line x1="-4" y1="14" x2="4" y2="14"/>
        <line x1="0" y1="-17" x2="0" y2="-20"/>
        <line x1="-12" y1="-12" x2="-14" y2="-14"/>
        <line x1="12" y1="-12" x2="14" y2="-14"/>
        <line x1="-16" y1="-1" x2="-19" y2="-1"/>
        <line x1="16" y1="-1" x2="19" y2="-1"/>
      </g>
      <!-- assessment: house with magnifier -->
      <circle cx="382" cy="58" r="29"/>
      <g transform="translate(382 58)">
        <path class="icon-stroke" d="M-15 -1 L-3 -13 L9 -1 M-12 -3 V12 H4"/>
        <rect class="icon-glyph" x="-7" y="3" width="5" height="9"/>
        <circle class="icon-stroke" cx="6" cy="4" r="6"/>
        <line class="icon-stroke" x1="10" y1="8" x2="16" y2="14" stroke-width="3.4"/>
      </g>
      <!-- problem: exclamation -->
      <circle cx="530" cy="58" r="29"/>
      <g class="icon-glyph" transform="translate(530 58)">
        <path d="M-4 -19 H4 L2 6 H-2 Z"/>
        <circle cx="0" cy="13" r="3.5"/>
      </g>
      <!-- solutions: puzzle piece -->
      <circle cx="626" cy="58" r="29"/>
      <path class="icon-glyph" transform="translate(626 58)" d="M-14 -8 H-5 C-8 -12 -6 -17 -1 -17 C4 -17 6 -12 3 -8 H10 V-1 C14 -4 18 -2 18 2 C18 6 14 8 10 5 V14 H2 C4 11 2 7 -2 7 C-6 7 -8 11 -6 14 H-14 Z"/>
      <!-- assess & select: tick -->
      <circle cx="758" cy="58" r="29"/>
      <path transform="translate(758 58)" d="M-14 0 L-4 10 L15 -10" fill="none" stroke="#ffffff" stroke-width="6" stroke-linecap="round" stroke-linejoin="round"/>
      <!-- report: document -->
      <circle cx="932" cy="58" r="29"/>
      <g transform="translate(932 58)">
        <path class="icon-glyph" d="M-11 -16 H5 L11 -10 V16 H-11 Z"/>
        <g stroke="var(--blue)" stroke-width="1.6">
          <line x1="-7" y1="-7" x2="7" y2="-7"/>
          <line x1="-7" y1="-2" x2="7" y2="-2"/>
          <line x1="-7" y1="3" x2="7" y2="3"/>
          <line x1="-7" y1="8" x2="7" y2="8"/>
        </g>
      </g>
      <!-- implement: gears -->
      <circle cx="1099" cy="58" r="29"/>
      <g transform="translate(1093 61)">
        <circle class="icon-glyph" r="9"/>
        <g class="icon-glyph">
          <rect x="-2.5" y="-13" width="5" height="26"/>
          <rect x="-13" y="-2.5" width="26" height="5"/>
          <rect x="-2.5" y="-13" width="5" height="26" transform="rotate(45)"/>
          <rect x="-2.5" y="-13" width="5" height="26" transform="rotate(-45)"/>
        </g>
        <circle r="3.5" fill="var(--blue)"/>
      </g>
      <g transform="translate(1108 50)">
        <circle class="icon-glyph" r="5"/>
        <rect class="icon-glyph" x="-1.6" y="-7.5" width="3.2" height="15"/>
        <rect class="icon-glyph" x="-7.5" y="-1.6" width="15" height="3.2"/>
        <circle r="2" fill="var(--blue)"/>
      </g>
      <g transform="translate(1110 69)">
        <circle class="icon-glyph" r="4.5"/>
        <rect class="icon-glyph" x="-1.5" y="-7" width="3" height="14"/>
        <rect class="icon-glyph" x="-7" y="-1.5" width="14" height="3"/>
        <circle r="1.8" fill="var(--blue)"/>
      </g>
    </g>

    <!-- step labels -->
    <text class="step-label step-label--lead" x="221" y="122">VISIONING</text>
    <text class="step-label step-label--minor" x="382" y="106">SPACE &amp; PHYSICAL</text>
    <text class="step-label step-label--minor" x="382" y="121">CONDITIONS ASSESSMENT</text>
    <text class="step-label step-label--minor" x="530" y="106">PROBLEM</text>
    <text class="step-label step-label--minor" x="530" y="121">DEFINED</text>
    <text class="step-label step-label--minor" x="626" y="105">IDENTIFY</text>
    <text class="step-label step-label--minor" x="626" y="120">SOLUTIONS</text>
    <text class="step-label step-label--major" x="758" y="121">ASSESS &amp; SELECT</text>
    <text class="step-label step-label--major" x="924" y="121">COMPILE REPORT</text>
    <text class="step-label step-label--major" x="1098" y="121">IMPLEMENT PLAN!</text>

    <!-- school row -->
    <g class="role role--school">
      <line x1="44" y1="134" x2="1099" y2="134" stroke="var(--school)" stroke-width="1.3"/>
      <circle cx="44" cy="134" r="19" fill="var(--school)"/>
      <g class="icon-glyph" transform="translate(44 134)">
        <path d="M-10 10 V-1 L0 -7 L10 -1 V10 Z"/>
        <rect x="-0.6" y="-13" width="1.2" height="6"/>
        <rect x="0" y="-13" width="4" height="3"/>
        <rect x="-2.5" y="3" width="5" height="7" fill="var(--school)"/>
        <rect x="-7.5" y="1" width="3" height="3" fill="var(--school)"/>
        <rect x="4.5" y="1" width="3" height="3" fill="var(--school)"/>
      </g>
      <text class="role-label role-label--spaced" x="70" y="146">SCHOOL</text>
      <g fill="var(--school)">
        <circle cx="221" cy="134" r="5"/>
        <circle cx="758" cy="134" r="5"/>
        <circle cx="1099" cy="134" r="5"/>
      </g>
    </g>

    <!-- architect row -->
    <g class="role role--architect">
      <line x1="44" y1="182" x2="1099" y2="182" stroke="var(--architect)" stroke-width="1.3"/>
      <circle cx="44" cy="182" r="19" fill="var(--architect)" role="img" aria-label="Architect avatar icon"/>
      <text class="role-label role-label--spaced" x="70" y="194" style="letter-spacing:1.6px">ARCHITECT</text>
      <g fill="var(--architect)">
        <circle cx="221" cy="182" r="5"/>
        <circle cx="388" cy="182" r="5"/>
        <circle cx="530" cy="182" r="5"/>
        <circle cx="626" cy="182" r="5"/>
        <circle cx="758" cy="182" r="5"/>
        <circle cx="932" cy="182" r="5"/>
        <circle cx="1099" cy="182" r="5"/>
      </g>
    </g>

    <!-- fundraising consultant row -->
    <g class="role role--fundraiser">
      <line x1="44" y1="231" x2="1099" y2="231" stroke="var(--fundraiser)" stroke-width="1.3"/>
      <circle cx="44" cy="231" r="19" fill="var(--fundraiser)" role="img" aria-label="Fundraising consultant avatar icon"/>
      <text class="role-label role-label--tight" x="70" y="242">FUNDRAISING</text>
      <text class="role-label role-label--tight" x="70" y="258">CONSULTANT</text>
      <g fill="var(--fundraiser)">
        <circle cx="221" cy="231" r="5"/>
        <circle cx="758" cy="231" r="5"/>
        <circle cx="1099" cy="231" r="5"/>
      </g>
    </g>
  </svg>

  <p class="caption">Image above depicts a general outline of the process developed by R&amp;M and used when conducting facilities master plans. The areas of responsibility are shown a circle for the group under a step, yet the groups (especially the school and the architect) are always working together towards the goal.</p>
</main>
</body>
</html>
```